Halvorn - Business Card Design

Design a modern masculine business card for our business

Target Market(s)

Private Market

Industry/Entity Type

Construction

Contact Information for Business Card

Company Name - Name of Person - Address - email address - contact number

Font styles to use
Serif
Sans Serif

Colors
0094D4
00A9DD
6FCCEA
C7EBF8
E9F6FB
00AB8E
00BBA5
67D7C9
C6EFE9
E9F9F6
F0912C
F2A743
F7CA91
FBE8D2
FDF5EE

Requirements
Must have
• Use company logo provided
Nice to have
• Company Logo

```html
<!DOCTYPE html>
<html lang="en">
<head>
<meta charset="utf-8">
<title>Halvorn Construction – Business Card</title>
<link rel="stylesheet" href="https://fonts.googleapis.com/css2?family=Montserrat:wght@700;800&family=Roboto:wght@400;500&display=swap">
<style>
  :root {
    --ink: #222222;
    --paper: #ffffff;
    --orange: #f26a21;
    --grey-text: #4a4a4a;
    --stage: #e7e7e7;
  }
  * { box-sizing: border-box; margin: 0; padding: 0; }
  html, body { width: 1200px; height: 900px; overflow: hidden; }
  body {
    background: var(--stage);
    font-family: "Roboto", Arial, sans-serif;
    position: relative;
  }
  .card {
    position: absolute;
    left: 300px;
    width: 600px;
    height: 343px;
    overflow: hidden;
    box-shadow: 0 6px 18px rgba(0,0,0,.18);
  }
  .card--back { top: 60px; background: var(--ink); }
  .card--front { top: 478px; background: var(--paper); }

  .brand {
    display: flex;
    align-items: center;
    gap: 12px;
    font-family: "Montserrat", Arial, sans-serif;
    font-weight: 800;
    letter-spacing: .02em;
    white-space: nowrap;
  }
  .brand__mark { background: var(--orange); flex: none; }

  .card--back .brand {
    position: absolute;
    inset: 0;
    justify-content: center;
    color: var(--paper);
    font-size: 30px;
  }
  .card--back .brand__mark { width: 26px; height: 26px; }

  .card--front .brand {
    position: absolute;
    top: 40px;
    right: 40px;
    color: var(--ink);
    font-size: 19px;
    gap: 9px;
  }
  .card--front .brand__mark { width: 16px; height: 16px; }

  .rule {
    position: absolute;
    left: 110px;
    right: 40px;
    top: 208px;
    height: 1px;
    background: var(--orange);
  }
  .side-tab {
    position: absolute;
    left: 0;
    top: 178px;
    width: 12px;
    height: 58px;
    background: var(--orange);
  }
  .person { position: absolute; left: 90px; top: 142px; }
  .person__name {
    font-family: "Montserrat", Arial, sans-serif;
    font-weight: 700;
    font-size: 26px;
    color: var(--orange);
    line-height: 1;
  }
  .person__role {
    font-size: 15px;
    color: var(--grey-text);
    letter-spacing: .03em;
    margin-top: 6px;
  }
  .contact {
    position: absolute;
    left: 110px;
    top: 222px;
    list-style: none;
    font-size: 15px;
    color: var(--grey-text);
  }
  .contact li { display: flex; align-items: center; gap: 8px; height: 22px; }
  .contact svg { width: 12px; height: 12px; flex: none; }
  .address {
    position: absolute;
    right: 45px;
    top: 232px;
    text-align: right;
    font-size: 14px;
    font-style: normal;
    line-height: 1.4;
    color: var(--grey-text);
  }
  .footer-band { position: absolute; left: 0; bottom: 0; width: 600px; height: 52px; }
</style>
</head>
<body>
  <section class="card card--back" aria-label="Card back">
    <div class="brand"><span class="brand__mark"></span>HALVORN CONSTRUCTION, INC</div>
  </section>

  <section class="card card--front" aria-label="Card front">
    <div class="brand"><span class="brand__mark"></span>HALVORN CONSTRUCTION, INC</div>

    <div class="side-tab"></div>
    <div class="person">
      <h1 class="person__name">DANIEL BROOKS</h1>
      <p class="person__role">DIRECTOR</p>
    </div>
    <div class="rule"></div>

    <ul class="contact">
      <li>
        <svg viewBox="0 0 12 12" aria-hidden="true"><path d="M2.5 1 L4.5 1 L5.2 3.6 L4 4.6 Q5 7 7.4 8 L8.4 6.8 L11 7.5 L11 9.5 Q10.5 11 9 11 Q1 10 1 3 Q1 1.5 2.5 1Z" fill="var(--orange)"/></svg>
        480-555-0142
      </li>
      <li>
        <svg viewBox="0 0 12 12" aria-hidden="true"><rect x="1" y="2.5" width="10" height="7" fill="none" stroke="var(--orange)" stroke-width="1.2"/><path d="M1 2.5 L6 6.5 L11 2.5" fill="none" stroke="var(--orange)" stroke-width="1.2"/></svg>
        info@halvornbuild.com
      </li>
      <li>
        <svg viewBox="0 0 12 12" aria-hidden="true"><circle cx="6" cy="6" r="5" fill="none" stroke="var(--orange)" stroke-width="1.1"/><ellipse cx="6" cy="6" rx="2.2" ry="5" fill="none" stroke="var(--orange)" stroke-width="1"/><path d="M1 6 H11" stroke="var(--orange)" stroke-width="1"/></svg>
        www.halvornbuild.com
      </li>
    </ul>

    <address class="address">
      1520 Harbor Lane<br>Los Angeles, CA 90021
    </address>

    <svg class="footer-band" viewBox="0 0 600 52" aria-hidden="true">
      <polygon points="0,44 470,14 470,52 0,52" fill="var(--ink)"/>
      <g fill="var(--orange)">
        <polygon points="474,14 490,14 484,52 468,52"/>
        <polygon points="496,14 512,14 506,52 490,52"/>
        <polygon points="518,14 534,14 528,52 512,52"/>
        <polygon points="540,14 556,14 550,52 534,52"/>
        <polygon points="562,14 578,14 572,52 556,52"/>
        <polygon points="584,14 600,14 600,52 578,52"/>
      </g>
    </svg>
  </section>
</body>
</html>
```